Clean Energy Brand - Business Card and Letterhead Designs

Hi, everyone! We need a graphic designer who has experience working with the energy sector. We want help designing a perfect two-sided business card and letterhead for a clean energy company we've been assisting. We have a great new logo and all of the associated files.Our client is looking for a design that is "disruptive," "future-facing," "masculine," "bold," and "empowering." The colours of the logo are navy blue and orange and are meant to stand out. We'll need all ownership and copyright paperwork as well as first proofs in a 48-hour period.

Target Market(s)

Government; Non-Profits; Clean Energy Industry; Municipalities; North American Energy Sector

Industry/Entity Type

Power Generation

Requirements
Must have
• A matching business card and letterhead design
Should not have
• Must not be from a template

```html
<!DOCTYPE html>
<html lang="en">
<head>
<meta charset="utf-8">
<title>Northvane – Business Card</title>
<link rel="stylesheet" href="https://fonts.googleapis.com/css2?family=Roboto:wght@400;700&display=swap">
<style>
  :root {
    --navy: #0b1c4a;
    --navy-mid: #2a3e6b;
    --orange: #ff5a14;
    --ink: #2b2b2b;
    --paper: #ffffff;
    --stage: #b1b2b6;
    --faint: #ececee;
  }
  * { margin: 0; padding: 0; box-sizing: border-box; }
  html, body { width: 1080px; height: 1200px; overflow: hidden; }
  body {
    background: var(--stage);
    font-family: "Roboto", Arial, sans-serif;
    position: relative;
  }
  .card {
    position: absolute;
    left: 120px;
    width: 840px;
    height: 525px;
    box-shadow: 4px 8px 10px rgba(0,0,0,0.35);
    overflow: hidden;
  }
  .card--front { top: 50px; background: var(--paper); }
  .card--back { top: 625px; background: var(--navy); }

  .brand {
    position: absolute;
    display: flex;
    align-items: center;
    gap: 16px;
    font-weight: 700;
    line-height: 1;
    letter-spacing: -1px;
  }
  .brand__dot {
    border-radius: 50%;
    background: var(--orange);
    flex: none;
  }
  .card--front .brand {
    left: 80px;
    top: 200px;
    color: var(--navy);
    font-size: 70px;
  }
  .card--front .brand__dot { width: 34px; height: 34px; }

  .front__decor {
    position: absolute;
    left: 549px;
    top: 18px;
    width: 252px;
    height: 258px;
    border-radius: 50%;
    background: radial-gradient(circle, var(--faint) 0%, rgba(236,236,238,0.6) 55%, rgba(255,255,255,0) 72%);
  }
  .front__bar {
    position: absolute;
    left: 803px;
    top: 290px;
    width: 37px;
    height: 198px;
    background: var(--navy);
  }
  .contact {
    position: absolute;
    right: 115px;
    top: 284px;
    list-style: none;
    color: var(--ink);
    font-size: 21px;
    line-height: 1.3;
  }
  .contact li {
    display: flex;
    justify-content: flex-end;
    align-items: center;
    gap: 22px;
    text-align: right;
  }
  .contact__icon { width: 24px; height: 24px; flex: none; }
  .contact__address { margin-bottom: 12px; }
  .contact__address .contact__icon { align-self: flex-start; margin-top: 2px; }
  .contact li + li:not(.contact__address) { margin-top: 3px; }

  .back__decor {
    position: absolute;
    inset: 0;
    background:
      radial-gradient(ellipse at 50% 50%, rgba(42,62,107,0.9) 0%, rgba(42,62,107,0.45) 45%, rgba(11,28,74,0) 75%),
      var(--navy);
  }
  .card--back .brand {
    left: 0;
    right: 0;
    top: 208px;
    justify-content: center;
    color: #ffffff;
    font-size: 90px;
  }
  .card--back .brand__dot { width: 40px; height: 40px; }
</style>
</head>
<body>
  <section class="card card--front">
    <div class="front__decor" role="img" aria-label="Faint large brand symbol as background decoration"></div>
    <div class="brand"><span class="brand__dot"></span><span class="brand__name">Northvane</span></div>
    <div class="front__bar"></div>
    <ul class="contact">
      <li class="contact__address">
        <span>Your Address Line<br>Your Sterrt 2000 View Location</span>
        <svg class="contact__icon" viewBox="0 0 24 24" fill="none" stroke="#ff5a14" stroke-width="1.5"><path d="M12 22s-7-7.5-7-12.5a7 7 0 0 1 14 0C19 14.5 12 22 12 22z"/><circle cx="12" cy="9.5" r="2.6"/></svg>
      </li>
      <li>
        <span>07 5550 1234</span>
        <svg class="contact__icon" viewBox="0 0 24 24" fill="none" stroke="#ff5a14" stroke-width="1.5"><path d="M5 3h4l2 5-2.5 1.5a11 11 0 0 0 6 6L16 13l5 2v4a2 2 0 0 1-2 2A16 16 0 0 1 3 5a2 2 0 0 1 2-2z"/></svg>
      </li>
      <li>
        <span>61 555 010 789</span>
        <svg class="contact__icon" viewBox="0 0 24 24" fill="none" stroke="#ff5a14" stroke-width="1.5"><rect x="6" y="2" width="12" height="20" rx="2"/><line x1="10" y1="18.5" x2="14" y2="18.5"/></svg>
      </li>
      <li>
        <span>hello@northvane.com</span>
        <svg class="contact__icon" viewBox="0 0 24 24" fill="none" stroke="#ff5a14" stroke-width="1.5"><rect x="2.5" y="5" width="19" height="14"/><path d="M2.5 5l9.5 8 9.5-8M2.5 19l7-7M21.5 19l-7-7"/></svg>
      </li>
      <li>
        <span>www.northvane.com</span>
        <svg class="contact__icon" viewBox="0 0 24 24" fill="none" stroke="#ff5a14" stroke-width="1.5"><circle cx="12" cy="12" r="9.5"/><ellipse cx="12" cy="12" rx="4" ry="9.5"/><line x1="2.5" y1="12" x2="21.5" y2="12"/></svg>
      </li>
    </ul>
  </section>

  <section class="card card--back">
    <div class="back__decor" role="img" aria-label="Large brand symbol in lighter navy spread across the card as background decoration"></div>
    <div class="brand"><span class="brand__dot"></span><span class="brand__name">Northvane</span></div>
  </section>
</body>
</html>
```